Bramblewick Keystone

Looking for modern business cards.
Clean contemporary design.
Similar to this.
https://www.snapvorlo.net/imgview?src=https%3A%2F%2Fcdn.printquell.net%2Fprofessional_elegant_modern_black_plain_metal_business_card-a1b2c3d4e5f60718293a4b5c6d7e8f90_qwxyz_4tmpl_540.jpg&ref=https%3A%2F%2Fwww.printquell.net%2Fprofessional_elegant_modern_black_plain_metal_business_card-100200300400500600&id=7aB9cD3e-QR5TU&tid=Xyz_abc123defGH%3A&v=10abcDEFghiJKLmnoPQRstUVwxYZ0123456789abcd..x&w=540&h=540&bih=1360&biw=1061&q=modern%20business%20cards&ref2=0abcDEFghiJKLmnoPQRstUVwxYZ0123456789abcd&ia=mrc&ua=8

But I'd like the blue to look metallic.

```html
<!DOCTYPE html>
<html lang="en">
<head>
<meta charset="utf-8">
<title>Bramblewick Keystone — Business Card</title>
<link href="https://fonts.googleapis.com/css2?family=Open+Sans:wght@400;600;700&display=swap" rel="stylesheet">
<style>
  :root {
    --backdrop: #2c2d2f;
    --paper: #f6f6f5;
    --ink: #454a4f;
    --navy: #1d4a68;
    --teal: #2a96b8;
    --teal-light: #5cc2dc;
    --teal-deep: #1b6f8c;
    --steel-dark: #1c5575;
    --steel-light: #3f86aa;
    --white: #ffffff;
  }
  * { margin: 0; padding: 0; box-sizing: border-box; }
  html, body { width: 1200px; height: 960px; overflow: hidden; }
  body {
    background: var(--backdrop);
    font-family: "Open Sans", Arial, sans-serif;
    position: relative;
  }
  .card {
    position: absolute;
    left: 250px;
    width: 700px;
    height: 400px;
    overflow: hidden;
    box-shadow: 0 14px 34px rgba(0,0,0,.45);
  }

  /* Back of card — metallic blue */
  .card-back {
    top: 40px;
    background:
      linear-gradient(115deg,
        rgba(255,255,255,0) 0%,
        rgba(255,255,255,.16) 38%,
        rgba(255,255,255,.32) 46%,
        rgba(255,255,255,.08) 54%,
        rgba(255,255,255,0) 70%,
        rgba(255,255,255,.14) 86%,
        rgba(255,255,255,0) 100%),
      linear-gradient(160deg, var(--teal-light) 0%, var(--teal) 35%, var(--teal-deep) 70%, var(--teal) 100%);
  }
  .back-brand {
    position: absolute;
    top: 150px; left: 0; right: 0;
    display: flex; align-items: center; justify-content: center; gap: 16px;
    color: var(--white);
    font-size: 38px;
    font-weight: 600;
    letter-spacing: .5px;
  }
  .brand-dot {
    width: 18px; height: 18px; border-radius: 50%;
    background: currentColor;
    flex: none;
  }
  .back-url {
    position: absolute;
    bottom: 34px; left: 0; right: 0;
    text-align: center;
    color: var(--white);
    font-size: 14px;
    letter-spacing: 3px;
  }

  /* Front of card */
  .card-front {
    top: 520px;
    background: var(--paper);
  }
  .front-brand {
    position: absolute;
    top: 42px; left: 58px;
    display: flex; align-items: center; gap: 12px;
    color: var(--teal);
    font-size: 30px;
    font-weight: 600;
  }
  .front-brand .brand-dot { width: 14px; height: 14px; }
  .address {
    position: absolute;
    top: 118px; left: 62px;
    color: var(--ink);
    font-size: 15px;
    line-height: 20px;
  }
  .contact-list {
    position: absolute;
    top: 168px; left: 40px;
    list-style: none;
    color: var(--ink);
    font-size: 15px;
    line-height: 22px;
  }
  .contact-list li { display: flex; align-items: center; gap: 10px; }
  .contact-list svg { width: 13px; height: 13px; fill: var(--navy); flex: none; }
  .person {
    position: absolute;
    right: 76px; bottom: 92px;
    text-align: left;
  }
  .person-name {
    color: var(--navy);
    font-size: 22px;
    font-weight: 700;
    letter-spacing: .5px;
  }
  .person-role {
    color: var(--teal);
    font-size: 16px;
    font-weight: 700;
    letter-spacing: .5px;
  }
  .base-band {
    position: absolute;
    left: 0; bottom: 0;
    width: 700px; height: 34px;
  }
</style>
</head>
<body>

  <section class="card card-back" aria-label="Card back">
    <div class="back-brand"><span class="brand-dot"></span>Bramblewick Keystone</div>
    <div class="back-url">www.bramblewickkeystone.com</div>
  </section>

  <section class="card card-front" aria-label="Card front">
    <div class="front-brand"><span>Bramblewick Keystone</span><span class="brand-dot"></span></div>

    <address class="address">
      412 Larchmere Court<br>
      Tarrowfield, Oregon 90417
    </address>

    <ul class="contact-list">
      <li>
        <svg viewBox="0 0 16 16" aria-hidden="true"><path d="M3.6 1.2 6 3.6 4.9 5.6c.9 2 2.6 3.7 4.6 4.6l2-1.1 2.4 2.4-1.6 2.3C7 13.6 2.4 9 1.3 2.8z"/></svg>
        555 210 4836
      </li>
      <li>
        <svg viewBox="0 0 16 16" aria-hidden="true"><path d="M4.5 0h7A1.5 1.5 0 0 1 13 1.5v13a1.5 1.5 0 0 1-1.5 1.5h-7A1.5 1.5 0 0 1 3 14.5v-13A1.5 1.5 0 0 1 4.5 0zM5 2v10h6V2zm3 11a1 1 0 1 0 0 2 1 1 0 0 0 0-2z"/></svg>
        555 374 9125
      </li>
      <li>
        <svg viewBox="0 0 16 16" aria-hidden="true"><path d="M4 1h8v4H4zM1 6h14v7h-3v2H4v-2H1zm4 5v3h6v-3z"/></svg>
        555 628 0473
      </li>
      <li>
        <svg viewBox="0 0 16 16" aria-hidden="true"><path d="M1 3h14v10H1zm1.5 1.3v.4L8 8.6l5.5-3.9v-.4z"/></svg>
        hello@bramblewickkeystone.com
      </li>
      <li>
        <svg viewBox="0 0 16 16" aria-hidden="true"><path d="M8 0a8 8 0 1 0 0 16A8 8 0 0 0 8 0zm-1 14.9A7 7 0 0 1 1.1 7H4c.1 2.9 1.3 5.9 3 7.9zM4 9H1.1M9 14.9C10.7 12.9 11.9 9.9 12 7h2.9A7 7 0 0 1 9 14.9zM6 7c.1-2.4 1-4.7 2-6 1 1.3 1.9 3.6 2 6z"/></svg>
        www.bramblewickkeystone.com
      </li>
    </ul>

    <div class="person">
      <div class="person-name">ELIAS MARROW</div>
      <div class="person-role">CEO/FOUNDER</div>
    </div>

    <svg class="base-band" viewBox="0 0 700 34" preserveAspectRatio="none" aria-hidden="true">
      <defs>
        <linearGradient id="steelBand" x1="0" y1="0" x2="1" y2="0">
          <stop offset="0" stop-color="#1c5575"/>
          <stop offset=".35" stop-color="#3f86aa"/>
          <stop offset=".55" stop-color="#1c5575"/>
          <stop offset=".85" stop-color="#2f7396"/>
          <stop offset="1" stop-color="#1c5575"/>
        </linearGradient>
        <linearGradient id="tealBand" x1="0" y1="0" x2="1" y2="0">
          <stop offset="0" stop-color="#1b6f8c"/>
          <stop offset=".35" stop-color="#5cc2dc"/>
          <stop offset=".6" stop-color="#2a96b8"/>
          <stop offset="1" stop-color="#1b6f8c"/>
        </linearGradient>
      </defs>
      <polygon points="0,12 390,12 380,34 0,34" fill="url(#steelBand)"/>
      <polygon points="398,12 700,12 700,34 388,34" fill="url(#tealBand)"/>
    </svg>
  </section>

</body>
</html>
```